Maplebright Savings Spree Promotional Postcard

I would like a postcard designed for a credit card balance transfer promotion.

The title for this promotion is "Maplebright savings spree".

(This paragraph should not be used word for word) Credit Card rates are on the rise since the Federal Prime Rate increase. I want to promote a non-variable rate credit card with rates as low as 7.9% APR* and free balance transfers. Simple, straightforward card with a low rate. There is no intro APR, always a great rate.

Below is some sample content options to highlight:
$0 Annual Fee
$0 Balance Transfer Fee
No Teaser, No Intro, just a great rate

Not only could you cut your interest rate in half, but you will also save hundreds of dollars by not paying any balance transfer fees.

Apply Today! www.tallowmerefin.org

Target Market(s)

Ages 25-45

Industry/Entity Type

Credit Card

Requirements
Must have
• Required disclaimer: *Annual Percentage Rate. 7.9% is the preferred rate based on qualifying credit. (teeny tiny disclaimer on front of card where rate is being advertised)
• Tagline: When you need OPTIONS ... (should be placed on back of postcard by credit union name, address, and logo)

```html
<!DOCTYPE html>
<html lang="en">
<head>
<meta charset="utf-8">
<title>Maplebright Savings Spree Postcard</title>
<link href="https://fonts.googleapis.com/css2?family=Lato:wght@400;700;900&display=swap" rel="stylesheet">
<style>
  :root {
    --navy: #27344f;
    --pink: #d3185b;
    --stage: #e6e6e6;
    --paper: #ffffff;
    --wood-light: #eceae6;
    --wood-mid: #cfcbc4;
    --rule: #c9c9c9;
  }
  * { box-sizing: border-box; margin: 0; padding: 0; }
  html, body { width: 1200px; height: 900px; overflow: hidden; }
  body {
    background: var(--stage);
    font-family: "Lato", sans-serif;
    color: var(--navy);
    position: relative;
  }
  .postcard {
    position: absolute;
    top: 267px;
    width: 548px;
    height: 366px;
    background: var(--paper);
    box-shadow: 0 4px 14px rgba(0,0,0,.18);
    overflow: hidden;
  }
  .postcard--front { left: 40px; }
  .postcard--back { left: 612px; }

  /* Front */
  .front-photo {
    position: absolute; inset: 0;
    background:
      radial-gradient(ellipse 120px 140px at 110px 230px, rgba(214,60,110,.35), transparent 70%),
      linear-gradient(180deg, var(--wood-light) 0%, #e4e2de 68%, var(--wood-mid) 100%);
  }
  .offer {
    position: absolute;
    left: 220px; right: 22px; top: 22px;
    text-align: center;
  }
  .offer__title { font-size: 29px; font-weight: 700; line-height: 1; text-align: right; }
  .offer__rate { display: flex; justify-content: flex-end; align-items: baseline; gap: 6px; margin-top: 2px; }
  .offer__rate-lead { font-size: 7px; font-weight: 700; letter-spacing: .3px; }
  .offer__rate-value { font-size: 27px; font-weight: 700; color: var(--pink); line-height: 1; }
  .offer__rate-apr { font-size: 8px; font-weight: 700; }
  .offer__headline { font-size: 20px; font-weight: 700; margin-top: 20px; }
  .offer__headline em { font-style: normal; color: var(--pink); }
  .offer__fees { display: flex; justify-content: center; align-items: center; gap: 14px; margin-top: 10px; }
  .offer__fee-amount { font-size: 36px; font-weight: 900; color: var(--pink); line-height: 1; }
  .offer__fee-list { text-align: left; font-size: 14px; line-height: 1.3; }
  .offer__plain { font-size: 14px; font-weight: 700; margin-top: 6px; }
  .offer__cta { font-size: 15px; font-weight: 700; color: var(--pink); margin-top: 22px; margin-right: 70px; }
  .offer__url { font-size: 14px; font-weight: 700; color: var(--pink); text-align: right; margin-top: 14px; }
  .disclaimer {
    position: absolute; right: 18px; bottom: 22px;
    font-size: 5.5px; color: var(--navy);
  }

  /* Back */
  .return-block { position: absolute; left: 22px; top: 20px; display: flex; gap: 14px; }
  .brand__name { font-size: 13px; font-weight: 700; color: var(--navy); display: flex; align-items: center; gap: 5px; }
  .brand__mark { width: 8px; height: 8px; background: var(--navy); }
  .brand__tagline { font-size: 9px; font-weight: 700; color: var(--pink); margin-top: 4px; }
  .return-address { font-size: 6px; line-height: 1.35; color: var(--pink); font-weight: 700; }
  .stamp-box {
    position: absolute; right: 20px; top: 24px;
    width: 90px; height: 70px;
    border: 1px solid var(--rule);
  }
  .address-lines { position: absolute; left: 276px; right: 20px; top: 140px; }
  .address-lines span { display: block; height: 1px; background: var(--rule); margin-bottom: 30px; }
</style>
</head>
<body>
  <section class="postcard postcard--front">
    <div class="front-photo" role="img" aria-label="Cupcake with white frosting and pink sprinkles, topped with a red paper honeycomb heart, on a weathered wooden table"></div>
    <div class="offer">
      <h1 class="offer__title">Velora credit cards</h1>
      <p class="offer__rate">
        <span class="offer__rate-lead">WITH RATES AS LOW AS</span>
        <span class="offer__rate-value">7.9%</span>
        <span class="offer__rate-apr">APR*</span>
      </p>
      <h2 class="offer__headline">it’s a <em>Maplebright</em> savings spree!</h2>
      <div class="offer__fees">
        <span class="offer__fee-amount">$0</span>
        <p class="offer__fee-list">Annual Fee<br>Balance Transfer Fee</p>
      </div>
      <p class="offer__plain">No Teaser, No Intro, just a great rate</p>
      <p class="offer__cta">Apply Today!</p>
      <p class="offer__url">www.tallowmerefin.org</p>
    </div>
    <p class="disclaimer">*Annual Percentage Rate. 7.9% is the preferred rate based on qualifying credit.</p>
  </section>

  <section class="postcard postcard--back">
    <div class="return-block">
      <div class="brand">
        <p class="brand__name"><span class="brand__mark"></span>Tallowmere Credit Union</p>
        <p class="brand__tagline">When you need OPTIONS ...</p>
      </div>
      <address class="return-address">
        Tallowmere Credit Union<br>
        1480 Birchfield Ave<br>
        Alder Springs, CO 80000<br>
        Phone: 555-010-0142<br>
        Fax: 555-010-0199
      </address>
    </div>
    <div class="stamp-box"></div>
    <div class="address-lines"><span></span><span></span><span></span><span></span><span></span></div>
  </section>
</body>
</html>
```